fieldscoutingpath.com - Social Media Branding

fieldscoutingpath.com --> Social Media Re-Branding & Graphics
Facebook: @fldscoutpath - Instagram: @fieldscoutingpath - Twitter: @fldscoutpath

Looking to find a good designer to help with my fieldscoutingpath.com social media sites!
- facebook banner
- twitter banner
- instagram template (square and banner size)
- Quote or Information Template
- Committed Template (uniformed) - see the ones I made (& i am no professional) at fieldscoutingpath.com/committed - needs to have fieldscoutingpath.com logo, room for: the committed school and the team the player plays on.

Also willing to pay extra for a graphic that is the "complete package" that detail all of the steps of the recruiting process detailed in fieldscoutingpath.com

Font styles to use
Sans Serif

Colors
ec1f27
fbee3e

```html
<!DOCTYPE html>
<html lang="en">
<head>
<meta charset="utf-8">
<title>fieldscoutingpath.com – Free Recruiting Seminar Banner</title>
<link rel="stylesheet" href="https://fonts.googleapis.com/css2?family=Roboto:wght@400;700&display=swap">
<style>
  :root {
    --brand-red: #ec1f27;
    --brand-yellow: #fbee3e;
    --ball-tone-a: #d2e23a;
    --ball-tone-b: #c3d62a;
    --white: #ffffff;
    --accent-line: #f4d21f;
  }
  html, body {
    margin: 0;
    padding: 0;
    width: 1200px;
    height: 400px;
    overflow: hidden;
    background: var(--white);
  }
  .banner {
    position: relative;
    width: 1200px;
    height: 400px;
    overflow: hidden;
    background: var(--brand-red);
    font-family: "Roboto", Arial, sans-serif;
    color: var(--white);
  }
  .banner-backdrop {
    position: absolute;
    inset: 0;
    width: 1200px;
    height: 400px;
  }
  .brand {
    position: absolute;
    left: 144px;
    top: 30px;
    display: flex;
    align-items: center;
    gap: 10px;
  }
  .brand-dot {
    width: 24px;
    height: 24px;
    border-radius: 50%;
    background: var(--brand-yellow);
  }
  .brand-name {
    font-weight: 700;
    font-size: 15px;
    color: var(--white);
    padding-bottom: 4px;
    border-bottom: 1px solid var(--white);
  }
  .event-title {
    position: absolute;
    left: 144px;
    top: 88px;
    margin: 0;
    font-size: 35px;
    line-height: 42px;
    font-weight: 700;
  }
  .event-audience {
    position: absolute;
    left: 145px;
    top: 182px;
    margin: 0;
    font-size: 19px;
    font-weight: 400;
  }
  .event-when {
    position: absolute;
    left: 840px;
    top: 88px;
    margin: 0;
    font-size: 35px;
    line-height: 42px;
    font-weight: 700;
  }
  .social-list {
    position: absolute;
    left: 840px;
    top: 187px;
    display: flex;
    gap: 14px;
    margin: 0;
    padding: 0;
    list-style: none;
  }
  .social-list li {
    width: 38px;
    height: 38px;
    border-radius: 50%;
    background: var(--white);
  }
  .softball-image {
    position: absolute;
    left: 457px;
    top: 42px;
    width: 320px;
    height: 320px;
    border-radius: 50%;
    background: linear-gradient(180deg, var(--ball-tone-a), var(--ball-tone-b));
  }
</style>
</head>
<body>
<div class="banner">
  <svg class="banner-backdrop" viewBox="0 0 1500 500" preserveAspectRatio="none" aria-hidden="true">
    <path class="wave-white" fill="#ffffff" d="M0,322 C300,285 600,330 800,388 C1000,428 1200,380 1500,300 L1500,500 L0,500 Z"/>
    <path class="wave-yellow" fill="#fbee3e" d="M0,358 C300,320 520,345 720,398 C920,446 1120,400 1500,338 L1500,500 L0,500 Z"/>
    <g class="accent-lines" stroke="#f4d21f" stroke-width="2" fill="none">
      <line x1="0" y1="212" x2="52" y2="262"/>
      <circle cx="59" cy="268" r="9"/>
      <line x1="1500" y1="62" x2="1316" y2="236"/>
      <circle cx="1309" cy="243" r="9"/>
    </g>
  </svg>

  <div class="brand">
    <span class="brand-dot"></span>
    <span class="brand-name">fieldscoutingpath.com</span>
  </div>

  <h1 class="event-title">Free Recruiting<br>Seminar</h1>
  <p class="event-audience">Player, Parents &amp; Coaches</p>

  <div class="softball-image" role="img" aria-label="Photo of a large yellow softball with red stitching"></div>

  <p class="event-when">Wednesday<br>7 PM ET</p>
  <ul class="social-list" aria-label="Social channels">
    <li></li>
    <li></li>
    <li></li>
  </ul>
</div>
</body>
</html>
```